Successful Health Company Needs a Face Lift

We need a beautiful new design for our existing, online health supplements business.

Most of the elements are already there, but we need your sophistication and style.

The 3 pages that need your magic touch are:
Home page:
http://www.vitalbloom.co.uk

Multiple Product pages. e.g:
http://www.vitalbloom.co.uk/health-issues/major-organs/skin-hair-nails.html

Single Product pages. e.g:
http://www.vitalbloom.co.uk/l-arginine-500-mg.html

Please have a look around.

This is a bilingual site, so all text (except logo) needs to be easily changed/translated. If photoshop files can be provided where we can simply translate the text layer of a graphic, that is acceptable. Please note that Greman words are generally longer than English.

Appearance:
The over all look should be open, light, uplifting and sophisticated.

The Home Page in detail:
We are largely happy with the category boxes in the centre column although you may restyle these if you wish.
The header, left menu and right column don't hang together and need your skills.

Logo:
We would like you to enhance our logo, but please note the 'S' and circle are used on many product labels, so we can't go too far from this just now.
(Product label example: http://www.vitalbloom.co.uk/black-walnut-tincture-from-green-hull.html)

Header:
This needs to imply health and be light and stylish without it taking up valuable room.

Left Menu:
This is a multi-layer concertina menu. It is hard to see where your are within it. It needs to be made more clear and easy to navigate, maybe by using indentation and or better colour choices.
Please show it expanded and condensed in your design proposals.
(Extended menu example: http://www.vitalbloom.co.uk/health-issues/female-health/thrush.html)

Multiple Product pages in detail
Please style the the brief descriptions, which must contain bullet points, price, add to basket and learn more.

Single Product pages in detail
The design and layout of this page needs to include all the elements currently there, including price, Qty, Add to Basket button, size and article number.

The static blocks on the right column will appear on these single product pages and need to suit the design well. They should not over-power the central content of the page.
Updates

Thank you all for participating.

Please note that what we are looking for is a more stylish and attractive version of what we already have.  The elements are all there.  We are not looking for a new concept.

We are happy for designers to switch images for better ones, work with colour ways, alter proportions and insert the elements in our brief.

We do not want to add banners, large images etc.  We want our customers to be familiar with what they see, and to be impressed with how much better the pages hang together.  They should not think they've landed at a new company.

We do want to see how the left menu looks when extended to show 2nd and 3rd tier menu titles.
We will also want to see how the design works for a multiple product page like this: http://www.vitalbloom.co.uk/supplement-type/anti-microbials.html
as well as a single product page like this:  http://www.vitalbloom.co.uk/black-walnut-extract.html

Some adjustment to the 'VitalBloom' logo is also an option and the graphic has been attached. 

Thank you for your careful attention to our brief.

Marcus.
pp Anselm

Project Deadline Extended
Reason: Due to unanticipated travel arrangements, the company director will only be available to make final decisions on Monday the 19th of March. Please continue updating submissions as we are in touch. Thank you for your understanding.

Target Market(s)

Health conscious women 70% men 30% aged 40 to 65 and health practitioners.

Industry/Entity Type

Health

Requirements
Must have
• Please include in the Header:
UK and German flags
Chatterbook, pok, +1, quiller, joined up, wander into
Padlock/SSL security/secure transaction
Practitioner helpline/ orders phone number
Fundwire/Credit card logo

Please include in right column:
Clinician Nook
Amalgam Clear Dental
Shopping Basket
Storefronts for Therapists

Please include in either Header or Right Column
Same day dispatch
Money back warranty

```html
<!DOCTYPE html>
<html lang="en">
<head>
<meta charset="utf-8">
<title>Vital Bloom Enterprises</title>
<link href="https://fonts.googleapis.com/css2?family=Arimo:wght@400;700&display=swap" rel="stylesheet">
<style>
:root{
  --pink:#f03e7e;
  --pink-deep:#d2588b;
  --pink-band:#e06b98;
  --pink-soft:#f5b9d3;
  --pink-pale:#f7e9f0;
  --page:#f1e4ec;
  --grey:#5e5e5e;
  --grey-light:#e2e2e2;
  --blue:#4bb6e3;
  --peach:#fad7b4;
  --gold:#e3b318;
  --white:#fff;
}
*{box-sizing:border-box;margin:0;padding:0}
html,body{width:1046px;height:1200px;overflow:hidden}
body{font-family:"Arimo",Arial,sans-serif;background:var(--page);color:var(--grey)}
.stage{width:1000px;height:1147px;transform:scale(1.046);transform-origin:0 0;position:relative;
  background:linear-gradient(var(--pink-band) 0 145px,var(--page) 145px)}
.sheet{position:absolute;left:33px;top:0;width:934px;height:1147px;background:var(--white)}
.abs{position:absolute}

/* header */
.brand{left:42px;top:22px;display:flex;align-items:center;gap:8px}
.brand-mark{width:68px;height:68px;border-radius:50%;border:5px solid var(--pink-deep);flex:none}
.brand-name{font-size:32px;color:var(--pink-deep);letter-spacing:.5px;line-height:1;white-space:nowrap}
.brand-sub{display:block;font-size:10px;letter-spacing:5px;margin-top:6px;text-align:right}
.helpline{left:398px;top:38px;font-size:15px;color:#444;line-height:19px}
.helpline strong{display:block;font-size:22px;color:var(--pink-deep);margin-top:4px;letter-spacing:.5px}
.secure{left:572px;top:40px;border-left:1px solid #ccc;padding-left:18px;height:60px;font-size:15px;color:#444}
.secure-row{display:flex;gap:3px;margin-top:12px;align-items:center}
.card-name{font-size:8px;border:1px solid #bbb;padding:4px 2px;color:#333;background:#f6f6f6}
.social{right:142px;top:7px;display:flex;gap:3px}
.social span{font-size:8px;background:#2d6ea8;color:#fff;padding:5px 3px;border-radius:2px}
.login{left:860px;top:5px;width:102px;height:24px;background:#eee;font-size:12px;color:#444;text-align:center;line-height:24px}
.cart{left:808px;top:40px;border-left:1px solid #ccc;padding-left:16px;height:60px;font-size:14px;color:#333}
.cart svg{display:block;margin-bottom:2px}
.cart em{font-style:normal;color:var(--pink-deep);font-size:12px;display:block;margin-top:4px}

/* nav */
.nav{left:38px;top:113px;width:925px;height:32px;background:var(--pink);border-radius:4px;display:flex;align-items:center}
.nav a{color:#fff;text-decoration:none;font-size:16px;padding:0 11px;border-right:1px solid #f8a0c0;line-height:22px}
.nav a:first-child{padding-left:18px}
.search{position:absolute;right:6px;top:4px;display:flex}
.search span{width:160px;height:24px;background:#fff;font-size:11px;color:#999;padding:6px 8px;border-radius:3px 0 0 3px}
.search b{height:24px;background:#e6e6e6;color:#333;font-size:12px;font-weight:400;padding:5px 8px;border-radius:0 3px 3px 0}

/* side menu */
.sidenav{left:38px;top:155px;width:194px;height:393px;background:var(--pink-soft);border-radius:3px;padding-top:8px}
.sidenav li{list-style:none;color:#fff;font-size:13px;height:28.5px;line-height:28.5px;padding:0 13px;border-bottom:1px solid #f8d3e3;display:flex;justify-content:space-between}
.sidenav li.gap{margin-top:4px}
.newsletter{left:38px;top:560px;width:194px}
.newsletter h3{font-weight:400;font-size:18px;color:#444}
.newsletter p{font-size:14px;color:#888}
.newsletter .field{height:30px;background:#eee;border:1px solid #ddd;border-radius:4px;margin-top:6px}
.newsletter .btn{display:inline-block;margin-top:10px;background:var(--blue);color:#fff;font-size:12px;padding:6px 11px;border-radius:4px}

/* category cards */
.cat{width:250px;height:158px;border:1px solid var(--grey-light);border-radius:6px;background:#fff}
.cat .tag{position:absolute;left:-6px;top:4px;background:var(--pink-deep);color:#fff;font-size:15px;padding:3px 12px;z-index:3;white-space:nowrap}
.cat ul{position:absolute;left:8px;top:37px;list-style:none;font-size:12.5px;line-height:18px;color:var(--grey);z-index:2;white-space:nowrap}
.cat .pic{position:absolute;right:0;top:0;width:125px;height:156px;border-radius:0 6px 6px 0;z-index:1}

/* right column */
.box{left:768px;width:195px;border:1px solid var(--grey-light);border-radius:5px;overflow:hidden;background:#fff}
.box h4{font-weight:400;font-size:16px;color:#222;background:#eee;padding:8px 9px;height:34px}
.box h4.sm{font-size:13px}
.box .photo{height:95px;position:relative;color:#fff;font-size:13px}
.box .photo span{position:absolute;left:8px;top:8px;width:130px}
.promo{left:768px;width:195px;border-radius:5px;display:flex;align-items:center}
.promo.blue{top:561px;height:89px;background:var(--blue);color:#fff;font-size:18px;padding-left:62px}
.promo.peach{top:659px;height:88px;background:var(--peach);color:#111;font-size:18px;padding-left:86px;font-weight:700}
.seal{left:810px;top:760px;width:100px;height:100px;border-radius:50%;background:var(--gold);border:6px solid #f2d460}

/* footer */
.links{left:38px;top:1025px;width:925px;height:78px;background:var(--pink-pale);font-size:11px;color:#333;text-align:center;line-height:18px;padding:11px 6px;white-space:nowrap}
.footer{left:38px;top:1110px;width:925px;height:32px;background:var(--pink-deep);color:#fff;font-size:12px;display:flex;align-items:center;justify-content:space-between;padding:0 10px 0 18px}
.footer nav{display:flex;gap:14px}
</style>
</head>
<body>
<div class="stage">
  <div class="sheet"></div>

  <header>
    <div class="abs brand">
      <span class="brand-mark"></span>
      <div class="brand-name">VITAL BLOOM<span class="brand-sub">ENTERPRISES</span></div>
    </div>
    <div class="abs helpline">Practitioner Helpline/<br>Orders Phone Number<strong>01632 480 215</strong></div>
    <div class="abs secure">100% Secure Founded 1996
      <div class="secure-row">
        <svg width="26" height="30" viewBox="0 0 26 30" aria-label="padlock"><path d="M7 13V9a6 6 0 0 1 12 0v4" fill="none" stroke="#999" stroke-width="3"/><rect x="3" y="13" width="20" height="16" rx="2" fill="#f2b820"/></svg>
        <span class="card-name">Meridian</span><span class="card-name">Amplex</span><span class="card-name">Veriso</span><span class="card-name">Fundwire</span><span class="card-name">Maestral</span>
      </div>
    </div>
    <div class="abs social"><span>pok</span><span>joined up</span><span>quiller</span><span>Chatterbook</span><span>wander into</span><span>+1</span></div>
    <div class="abs login">Log In | Register</div>
    <div class="abs cart">
      <svg width="30" height="24" viewBox="0 0 30 24" aria-label="basket"><path d="M3 9h24l-3 13H6z" fill="#7cbf2e"/><path d="M9 9l6-7 6 7" fill="none" stroke="#555" stroke-width="2"/></svg>
      Shopping Cart<em>Your cart is empty</em>
    </div>
    <nav class="abs nav">
      <a>Home</a><a>Detox</a><a>Hydration</a><a>Supplements</a><a>Your Health Issues</a>
      <div class="search"><span>Search</span><b>Search</b></div>
    </nav>
  </header>

  <aside class="abs sidenav">
    <ul>
      <li>A to Z</li>
      <li>Supplement Type<span>+</span></li>
      <li>Your Health Issue<span>+</span></li>
      <li>Expert Product Lines<span>+</span></li>
      <li class="gap">Detox &amp; Cleansing<span>+</span></li>
      <li>Hydration &amp; Water<span>+</span></li>
      <li>Natural Body Care<span>+</span></li>
      <li class="gap">Sport &amp; Fitness</li>
      <li>Health Technology</li>
      <li>Household Products</li>
      <li class="gap">Laboratory Tests</li>
      <li>Books &amp; Education</li>
      <li>New &amp; Special Offers</li>
    </ul>
  </aside>
  <div class="abs newsletter">
    <h3>Newsletter</h3><p>Sign up for our newsletter:</p>
    <div class="field"></div><span class="btn">SUBSCRIBE</span>
  </div>

  <main>
    <section class="abs cat" style="left:246px;top:155px"><span class="tag">DIGESTION</span><ul><li>Constipation</li><li>Candida</li><li>Irritable Bowel</li><li>Wind</li></ul><div class="pic" role="img" aria-label="Woman's midriff" style="background:linear-gradient(90deg,#fff,#ead2c3 45%,#e4c4b2)"></div></section>
    <section class="abs cat" style="left:510px;top:155px"><span class="tag">PAIN</span><ul><li>Back Pain</li><li>Joint and Bone</li><li>Headaches</li><li>Period Pain</li></ul><div class="pic" role="img" aria-label="Man holding sore neck" style="background:linear-gradient(90deg,#fff,#c98b6f 45%,#a9654b)"></div></section>
    <section class="abs cat" style="left:246px;top:329px"><span class="tag">WEIGHT LOSS</span><ul><li>Constipation</li><li>Candida</li><li>Irritable Bowel</li><li>Wind</li></ul><div class="pic" role="img" aria-label="Woman measuring waist" style="background:linear-gradient(90deg,#fff,#d9b29c 45%,#3a3a3a)"></div></section>
    <section class="abs cat" style="left:510px;top:329px"><span class="tag">FEMALE HEALTH</span><ul><li>Breast Health</li><li>Menopause</li><li>Menstruation &amp; PMT</li></ul><span class="tag" style="top:90px;left:0">MALE HEALTH</span><ul style="top:118px"><li>Erectile Dysfunction</li><li>Hair Loss.&nbsp; Prostate Health</li></ul><div class="pic" role="img" aria-label="Male and female symbols" style="background:linear-gradient(160deg,#fff 20%,#4aa0e0 45%,#fff 60%,#f06bc0 85%,#fff)"></div></section>
    <section class="abs cat" style="left:246px;top:503px"><span class="tag">DETOX</span><ul><li>Heavy Metal Detox</li><li>Parasite Cleanse</li><li>Kidney Cleanse</li><li>Liver Cleanse</li><li>Colon Cleanse</li></ul><div class="pic" role="img" aria-label="Fresh dill herb" style="background:radial-gradient(circle at 55% 50%,#4f9a2a,#8cc95a 45%,#fff 70%)"></div></section>
    <section class="abs cat" style="left:510px;top:503px"><span class="tag">BODY CARE</span><ul><li>Anti Aging</li><li>Cosmetics</li><li>Skin Range</li><li>Face &amp; Mouth</li><li>Hair Care</li></ul><div class="pic" role="img" aria-label="Woman with smooth skin" style="background:linear-gradient(90deg,#fff,#f0d4bf 45%,#e6bf9f)"></div></section>
    <section class="abs cat" style="left:246px;top:677px"><span class="tag">BRAIN HEALTH</span><ul><li>Memory</li><li>Headaches</li><li>Cognitive Function</li><li>Mood &amp; Sleep</li></ul><div class="pic" role="img" aria-label="Head with brain illustration" style="background:linear-gradient(90deg,#fff,#f3d3ce 45%,#e8a7a0)"></div></section>
    <section class="abs cat" style="left:510px;top:677px"><span class="tag">WATER &amp; HYDRATION</span><ul><li>Water Filtration</li><li>Electrolytes</li><li>Super-Hydration</li></ul><div class="pic" role="img" aria-label="Water splash" style="background:radial-gradient(ellipse at 50% 70%,#7fc3e8,#cfe9f6 45%,#fff 70%)"></div></section>
    <section class="abs cat" style="left:246px;top:851px"><span class="tag">HEALTH DEVICES</span><ul><li>Memory</li><li>Headaches</li><li>Cognitive Function</li><li>Mood &amp; Sleep</li></ul><div class="pic" role="img" aria-label="Red heart with stethoscope" style="background:radial-gradient(circle at 55% 45%,#e02626,#f08a8a 35%,#fff 65%)"></div></section>
    <section class="abs cat" style="left:510px;top:851px"><span class="tag">CARDIOVASCULAR</span><ul><li>Water Filtration</li><li>Electrolytes</li><li>Super-Hydration</li></ul><div class="pic" role="img" aria-label="Torso with heart anatomy" style="background:linear-gradient(90deg,#fff,#e5b79c 40%,#c9856a)"></div></section>
  </main>

  <aside>
    <div class="abs box" style="top:155px;height:130px"><h4>CLINICIAN NOOK</h4><div class="photo" role="img" aria-label="Woman relaxing in meadow" style="background:linear-gradient(#6b8c3a,#9cc456 60%,#f1d7b6)"><span>Contact a Natural Health Practitioner</span></div></div>
    <div class="abs box" style="top:295px;height:130px"><h4 class="sm">AMALGAM CLEAR DENTAL</h4><div class="photo" role="img" aria-label="Smiling mouth with white teeth" style="background:linear-gradient(90deg,#d9eef8,#f2d3c5)"><span style="top:auto;bottom:6px;color:#1a7fb5">A comprehensive list available here.</span></div></div>
    <div class="abs box" style="top:435px;height:116px"><h4 class="sm">SHOPPING BASKET</h4>
      <p style="position:absolute;left:12px;top:50px;width:110px;font-size:13px;color:#444">You have no items in your shopping basket.</p>
      <svg style="position:absolute;left:126px;top:42px" width="60" height="60" viewBox="0 0 60 60" aria-label="basket"><path d="M18 24l12-18 12 18" fill="none" stroke="#2a6d99" stroke-width="3"/><path d="M4 24h52l-6 30H10z" fill="#3aa3d8"/><path d="M18 30v18M26 30v18M34 30v18M42 30v18" stroke="#fff" stroke-width="3"/></svg>
    </div>
    <div class="abs promo blue" role="img" aria-label="Therapist giving thumbs up">Storefronts for Therapists</div>
    <div class="abs promo peach">
      <svg style="position:absolute;left:12px;top:14px" width="60" height="60" viewBox="0 0 60 60" aria-label="delivery truck"><rect x="4" y="6" width="52" height="38" rx="4" fill="#b5541a"/><rect x="12" y="12" width="36" height="14" fill="var(--peach)"/><circle cx="16" cy="50" r="7" fill="#b5541a"/><circle cx="44" cy="50" r="7" fill="#b5541a"/></svg>
      SAME DAY DISPATCH
    </div>
    <div class="abs seal" role="img" aria-label="Guarantee seal"></div>
  </aside>

  <footer>
    <div class="abs links">Kidney Pain &nbsp;|&nbsp; Kidney Stones &nbsp;|&nbsp; Kidney Disease Symptoms &nbsp;|&nbsp; Colon Cleanse &nbsp;|&nbsp; Digestive Enzymes &nbsp;|&nbsp; Digestive Enzymes Supplement &nbsp;|&nbsp; Healing Principles &nbsp;|&nbsp; Herbal Remedies<br>Herbal Remedies for Anxiety &nbsp;|&nbsp; Herbal Remedies for Constipation &nbsp;|&nbsp; Herbal Remedies for Depression &nbsp;|&nbsp; Herbal Remedies for Menopause &nbsp;|&nbsp; Bloated Stomach &nbsp;|&nbsp; Health Shops<br>|&nbsp; Nutrelle &nbsp;|&nbsp; What is Amalgam Clear Dental?</div>
    <div class="abs footer"><span>© 2010 Vital Bloom Enterprises. All Rights Reserved.</span>
      <nav><span>About Us</span><span>Search Terms</span><span>Advanced Search</span><span>Terms &amp; Conditions</span><span>Privacy Policy</span><span>Contact Us</span></nav>
    </div>
  </footer>
</div>
</body>
</html>
```